Financial Advisor Resource Firm needs business card design

Need business card design for company in Omaha NE called Tallowbrook Partners. We provide resources to financial advisors....workshop programs, retirement analysis, and insurance planning. I would like to see designs that use grays, greens, black, and white colors. The final design should communicate 'collaboration' and be simple yet attractive to financial planning clients. I will attached our logo and another picture of a puzzle piece coming together. I would like the incorporate the puzzle picture somehow, maybe on the back somehow, with color or just the gray scale....OR, the picture be the front of the card with 'Tallowbrook' definition on it (see upload) and then company logo, employee name, title, address on the back (see ppt uploaded). The following disclosure needs to be included somewhere- Advisory services offered through Marlowe Ridge Advisors, LLC.
Updates

I uploaded a svg and ai file of the logo

Target Market(s)

Financial planning clients and financial advisors....so pretty diverse age range of about 40-70.

Industry/Entity Type

Financial Planning

Contact Information for Business Card

Dennis K. Holloway, MBA
Founder/President
5727 E. Larkspur Avenue
Suite 418
Omaha, NE 68297
Phone- (402) 555-0147
Cell- (402) 555-0183
Fax- (402) 555-0129
email- dennis@tallowbrookgroup.example
web address- www.tallowbrookgroup.example

Colors
1b1b1b
474747
d3d3d3
ffffff
9bcb3c
abd036

Requirements
Must have
• Must include logo provided, must be 2 sided, and must have disclosure...all of these items listed in project description

```html
<!DOCTYPE html>
<html lang="en">
<head>
<meta charset="utf-8">
<title>Tallowbrook Partners – Business Card</title>
<link rel="stylesheet" href="https://fonts.googleapis.com/css2?family=Poppins:wght@300;400;600&display=swap">
<style>
  :root {
    --ink: #1b1b1b;
    --charcoal: #262626;
    --slate: #474747;
    --mist: #d3d3d3;
    --paper: #ffffff;
    --green: #9bcb3c;
    --lime: #abd036;
    --backdrop: #e4e4e4;
  }
  * { margin: 0; padding: 0; box-sizing: border-box; }
  html, body { width: 1200px; height: 800px; overflow: hidden; }
  body {
    background: var(--backdrop);
    font-family: "Poppins", sans-serif;
    position: relative;
  }
  .card {
    position: absolute;
    top: 138px;
    width: 300px;
    height: 525px;
    overflow: hidden;
    box-shadow: 0 10px 28px rgba(0,0,0,0.22);
  }
  .card--front { left: 270px; background: var(--paper); }
  .card--back { left: 630px; background: var(--charcoal); }

  .card__waves { position: absolute; inset: 0; width: 300px; height: 525px; }

  .brand {
    position: absolute;
    left: 0; right: 0;
    text-align: center;
    font-weight: 600;
    font-size: 21px;
    letter-spacing: 0.5px;
  }
  .brand--front { top: 100px; color: var(--ink); }
  .brand--back { top: 200px; color: var(--paper); }

  .contact {
    position: absolute;
    left: 0; top: 275px;
    width: 300px;
    padding-left: 34px;
    color: var(--paper);
  }
  .contact__marker {
    position: absolute;
    left: 0; top: 2px;
    width: 9px; height: 32px;
    background: var(--green);
  }
  .contact__name {
    color: var(--green);
    font-weight: 600;
    font-size: 15px;
    letter-spacing: 0.3px;
    line-height: 20px;
  }
  .contact__title { font-size: 12px; font-weight: 300; margin-top: 2px; }
  .contact__company {
    color: var(--green);
    font-size: 13px;
    font-weight: 600;
    margin-top: 14px;
  }
  .contact__address { font-size: 12px; font-weight: 300; line-height: 19px; margin-top: 2px; }

  .contact-list { list-style: none; margin-top: 18px; }
  .contact-list li {
    display: flex;
    align-items: center;
    gap: 12px;
    font-size: 12px;
    font-weight: 300;
    height: 19px;
  }
  .contact-list svg { width: 13px; height: 13px; flex: none; }
  .accent { color: var(--green); }

  .web-address {
    position: absolute;
    left: 34px; top: 420px;
    color: var(--paper);
    font-size: 12.5px;
    letter-spacing: 1.6px;
    font-weight: 300;
  }
  .disclosure {
    position: absolute;
    left: 20px; right: 20px; bottom: 22px;
    text-align: center;
    color: var(--mist);
    font-size: 8.5px;
    font-weight: 300;
    letter-spacing: 0.3px;
    line-height: 12px;
  }
</style>
</head>
<body>

<section class="card card--front" aria-label="Card front">
  <svg class="card__waves" viewBox="0 0 300 525" aria-hidden="true">
    <path d="M0 232 Q150 180 300 226 L300 525 L0 525 Z" fill="#9bcb3c"/>
    <path d="M0 246 Q150 196 300 240 L300 525 L0 525 Z" fill="#262626"/>
  </svg>

  <div class="brand brand--front">Tallowbrook Partners</div>

  <div class="contact">
    <span class="contact__marker"></span>
    <p class="contact__name">DENNIS K. HOLLOWAY, MBA</p>
    <p class="contact__title">Founder / President</p>
    <p class="contact__company">Tallowbrook Group</p>
    <p class="contact__address">5727 E. Larkspur Avenue<br>Suite 418</p>

    <ul class="contact-list">
      <li>
        <svg viewBox="0 0 14 14"><circle cx="7" cy="7" r="7" fill="#9bcb3c"/><path d="M4.5 3.5l1.5 1.5-.8 1a5 5 0 002.8 2.8l1-.8 1.5 1.5-1 1C6.5 10.5 3.5 7.5 3.5 4.5z" fill="#fff"/></svg>
        (402) 555-0147
      </li>
      <li>
        <svg viewBox="0 0 14 14"><circle cx="7" cy="7" r="7" fill="#9bcb3c"/><rect x="5" y="3" width="4" height="8" rx="0.8" fill="#fff"/></svg>
        (402) 555-0183
      </li>
      <li>
        <svg viewBox="0 0 14 14"><circle cx="7" cy="7" r="7" fill="#9bcb3c"/><rect x="3.5" y="6" width="7" height="4" rx="0.6" fill="#fff"/><rect x="5" y="3.5" width="4" height="2" fill="#fff"/></svg>
        (402) 555-0129
      </li>
      <li>
        <svg viewBox="0 0 14 14"><circle cx="7" cy="7" r="7" fill="#9bcb3c"/><rect x="3.5" y="4.5" width="7" height="5" fill="#fff"/><path d="M3.5 4.5L7 7.3l3.5-2.8" fill="none" stroke="#9bcb3c" stroke-width="0.8"/></svg>
        dennis@tallowbrookgroup.example
      </li>
      <li>
        <svg viewBox="0 0 14 14"><circle cx="7" cy="7" r="7" fill="#9bcb3c"/><circle cx="7" cy="7" r="3.6" fill="none" stroke="#fff" stroke-width="0.9"/><path d="M3.4 7h7.2M7 3.4v7.2" stroke="#fff" stroke-width="0.7"/></svg>
        <span>www.<span class="accent">tallowbrookgroup</span>.example</span>
      </li>
    </ul>
  </div>
</section>

<section class="card card--back" aria-label="Card back">
  <div class="brand brand--back">Tallowbrook Partners</div>
  <p class="web-address">www.<span class="accent">tallowbrookgroup</span>.example</p>
  <p class="disclosure">Advisory services offered through Marlowe Ridge Advisors, LLC.</p>
</section>

</body>
</html>
```